Packing for Disinfectant wipes

Design the Packinging for new Disinfectant wipes. Wipes are for cleaning and disinfectanting hard surfaces and equipment. There are 100 wipes to the packet (size 230mm x 300mm). The company is called Norbeck Supplies and is supplier of consumable products to healthcare companies. Wipes are not for use on humans/baby. Packaging size as per attachment.
Industry/Entity Type
Healthcare
Requirements
Nice to have
- Packaging need ingredients list and directions for use

```html
<!DOCTYPE html>
<html lang="en">
<head>
<meta charset="utf-8">
<title>Norbeck Supplies – Disinfectant Wipes Pack</title>
<link rel="stylesheet" href="https://fonts.googleapis.com/css2?family=Roboto+Condensed:wght@500;700&family=Roboto:wght@300&display=swap">
<style>
  :root {
    --bg: #e4e4e4;
    --blue-deep: #16368e;
    --blue-mid: #2f56ad;
    --blue-light: #4a72c0;
    --green-dark: #2f8f12;
    --green-mid: #4cad1c;
    --green-light: #79cc2a;
    --silver: #c9ccd2;
    --white: #ffffff;
  }
  html, body {
    margin: 0;
    padding: 0;
    width: 1200px;
    height: 960px;
    overflow: hidden;
    background: var(--bg);
  }
  .canvas {
    position: relative;
    width: 1200px;
    height: 960px;
  }
  .pack {
    position: absolute;
    left: 0;
    top: 0;
    width: 1200px;
    height: 960px;
  }
  .brand-name {
    font-family: "Roboto", sans-serif;
    font-weight: 300;
    font-size: 22px;
    fill: var(--white);
  }
  .product-title {
    font-family: "Roboto Condensed", sans-serif;
    font-weight: 700;
    font-size: 50px;
    fill: var(--white);
  }
  .claim {
    font-family: "Roboto Condensed", sans-serif;
    font-weight: 700;
    font-size: 10.5px;
    fill: var(--white);
  }
  .count-number {
    font-family: "Roboto Condensed", sans-serif;
    font-weight: 700;
    font-size: 21px;
    fill: var(--white);
  }
  .count-label {
    font-family: "Roboto Condensed", sans-serif;
    font-weight: 500;
    font-size: 11px;
    fill: var(--white);
  }
  .icon-ring {
    fill: none;
    stroke: var(--white);
    stroke-width: 2.5;
  }
</style>
</head>
<body>
<div class="canvas">
  <svg class="pack" viewBox="0 0 1200 960" xmlns="http://www.w3.org/2000/svg">
    <defs>
      <linearGradient id="blueFill" x1="0" y1="0" x2="1" y2="1">
        <stop offset="0" stop-color="#1a3a92"/>
        <stop offset="0.5" stop-color="#3358ad"/>
        <stop offset="1" stop-color="#102a78"/>
      </linearGradient>
      <linearGradient id="greenFill" x1="0" y1="0" x2="1" y2="0">
        <stop offset="0" stop-color="#5bb52a"/>
        <stop offset="0.45" stop-color="#74c62a"/>
        <stop offset="1" stop-color="#2f8a12"/>
      </linearGradient>
      <linearGradient id="sealFill" x1="0" y1="0" x2="1" y2="0">
        <stop offset="0" stop-color="#2a4fa6"/>
        <stop offset="1" stop-color="#1b3b8f"/>
      </linearGradient>
      <linearGradient id="emblemFill" x1="0" y1="0" x2="0" y2="1">
        <stop offset="0" stop-color="#7dd12a"/>
        <stop offset="1" stop-color="#3a9a18"/>
      </linearGradient>
      <clipPath id="bodyClip">
        <rect x="222" y="214" width="791" height="526" rx="40"/>
      </clipPath>
      <clipPath id="lidClip">
        <rect x="456" y="342" width="364" height="231" rx="52"/>
      </clipPath>
    </defs>

    <!-- end seals -->
    <rect class="seal seal-left" x="185" y="280" width="40" height="396" rx="3" fill="url(#sealFill)"/>
    <rect class="seal seal-right" x="1010" y="283" width="40" height="393" rx="3" fill="url(#sealFill)"/>

    <!-- pack body -->
    <g class="pack-body" clip-path="url(#bodyClip)">
      <rect x="222" y="214" width="791" height="526" fill="url(#greenFill)"/>
      <path d="M222 214 H1013 V280 C900 430 760 560 600 575 C450 585 320 480 222 320 Z" fill="url(#blueFill)"/>
      <path d="M222 320 C320 480 450 585 600 575 C760 560 900 430 1013 280 L1013 300 C900 455 760 580 600 590 C440 598 315 500 222 345 Z" fill="var(--silver)"/>
    </g>

    <!-- brand -->
    <g class="brand">
      <rect x="566" y="273" width="12" height="12" fill="var(--white)"/>
      <text class="brand-name" x="586" y="286">Norbeck Supplies</text>
    </g>

    <!-- lid -->
    <g class="lid">
      <g clip-path="url(#lidClip)">
        <rect x="456" y="342" width="364" height="231" fill="url(#greenFill)"/>
        <path d="M456 342 H820 V430 C740 475 680 508 600 510 C540 512 490 495 456 470 Z" fill="url(#blueFill)"/>
        <path d="M456 470 C490 495 540 512 600 510 C680 508 740 475 820 430 L820 442 C740 490 680 522 600 526 C535 528 488 510 456 487 Z" fill="var(--silver)"/>
      </g>
      <rect x="456" y="342" width="364" height="231" rx="52" fill="none" stroke="#1f3f95" stroke-width="2"/>
      <text class="product-title" x="511" y="409" textLength="253" lengthAdjust="spacingAndGlyphs">DISINFECTANT</text>
      <text class="product-title" x="511" y="461" textLength="111" lengthAdjust="spacingAndGlyphs">WIPES</text>

      <!-- emblem placeholder -->
      <rect class="emblem-placeholder" x="638" y="424" width="128" height="140" rx="14"
            fill="url(#emblemFill)" role="img"
            aria-label="Emblem: green shield with white cross and blue arrow"/>
    </g>

    <!-- germ claim -->
    <g class="germ-claim">
      <circle cx="393" cy="615" r="21" class="icon-ring"/>
      <circle cx="393" cy="615" r="15" fill="var(--green-light)" role="img" aria-label="Germ icon crossed out"/>
      <text class="claim" x="393" y="653" text-anchor="middle">KILLS 99.9%</text>
      <text class="claim" x="393" y="664" text-anchor="middle">OF GERMS*</text>
    </g>

    <!-- surface use icons -->
    <g class="surface-icons">
      <circle cx="514" cy="637" r="21" class="icon-ring"/>
      <circle cx="514" cy="637" r="15" fill="var(--green-light)" role="img" aria-label="Toilet surface icon"/>
      <circle cx="579" cy="637" r="21" class="icon-ring"/>
      <circle cx="579" cy="637" r="15" fill="var(--green-light)" role="img" aria-label="Washing machine surface icon"/>
      <circle cx="644" cy="637" r="21" class="icon-ring"/>
      <circle cx="644" cy="637" r="15" fill="var(--green-light)" role="img" aria-label="Floor tiles surface icon"/>
      <circle cx="709" cy="637" r="21" class="icon-ring"/>
      <circle cx="709" cy="637" r="15" fill="var(--green-light)" role="img" aria-label="Home surface icon"/>
    </g>

    <!-- wipe count -->
    <g class="wipe-count">
      <text class="count-number" x="840" y="640">100</text>
      <text class="count-label" x="841" y="653">WIPES</text>
      <circle cx="894" cy="638" r="14" class="icon-ring"/>
      <circle cx="894" cy="638" r="9" fill="#4aa81a" role="img" aria-label="Not for use on people or babies icon"/>
    </g>
  </svg>
</div>
</body>
</html>
```